Web Design for One for One Organic Soap Company

We need a website design for the company Tidewell Botanics based on the package design per attached.

The design should communicate high end, luxury organic. The site will provide facts about how the spread of disease causes deaths and can be prevented with hand washing. The site will also have a page about why we are passionate about organics and how that relates to our skin including skin facts.
Also, the site should have an e-commerce product page and shopping cart.

Target Market(s)

Educated, health conscious and socially conscious consumers who shop luxury. Target vendors include Larkmont Grocers and Velbrook..

Industry/Entity Type

E-Commerce

Font styles to use
Other font styles liked:
• See attached

Requirements
Must have
• Use of Ying Yang leaf Logo provided.
Based on design provided.

```html
<!DOCTYPE html>
<html lang="en">
<head>
<meta charset="utf-8">
<title>Tidewell Botanics – Organic Soap</title>
<link href="https://fonts.googleapis.com/css2?family=Open+Sans:ital,wght@0,400;0,600;0,700;1,400&family=Merriweather:wght@400;700&display=swap" rel="stylesheet">
<style>
:root{
  --paper:#e4e0d4;
  --paper-dark:#d6d1c3;
  --band:#6b675f;
  --band-dark:#5a5650;
  --rust:#b3432a;
  --rust-soft:#c8553b;
  --brown:#7a4a2a;
  --ink:#333;
  --muted:#666;
  --panel:#f2f2f2;
  --rule:#d9d9d9;
  --footer:#3a3a3a;
  --footer-text:#e6e6e6;
  --bar:#6e6e6e;
}
*{box-sizing:border-box;margin:0;padding:0}
html,body{width:892px;height:1200px;overflow:hidden}
body{position:relative;background:var(--paper);font-family:"Open Sans",Arial,sans-serif;color:var(--ink)}
.abs{position:absolute}
.site-header{left:0;top:0;width:892px;height:100px;background:linear-gradient(#dcd8cb,var(--paper))}
.brand{left:86px;top:28px;display:flex;align-items:center;gap:8px}
.brand-mark{width:38px;height:58px;background:var(--rust)}
.brand-name{font-size:19px;font-weight:400;color:var(--brown);line-height:26px}
.brand-tag{font-size:15px;color:var(--brown);line-height:22px;letter-spacing:1px}
.util-links{left:585px;top:35px;font-size:10.5px;color:#555;word-spacing:2px}
.util-links span{margin:0 6px}
.search{left:584px;top:57px;width:156px;height:20px;background:#efece4;border:1px solid #cfcabd;font-size:9px;color:#999;padding:3px 8px}
.search-btn{left:722px;top:57px;width:18px;height:20px;background:#4a4a4a}
.cart{left:750px;top:61px;font-size:9.5px;color:#555}
.cart-count{left:774px;top:61px;width:24px;height:13px;background:#d65a1d;color:#fff;font-size:8px;text-align:center;line-height:13px;border-radius:2px}
.main-nav{left:0;top:100px;width:892px;height:70px;background:linear-gradient(var(--band),var(--band-dark));}
.main-nav ul{list-style:none;display:flex;position:absolute;left:83px;top:18px}
.main-nav li{color:#f2f2f2;font-size:11.5px;height:26px;line-height:26px;padding:0 13px;text-transform:uppercase;border-right:1px dashed #8a867e}
.main-nav li:last-child{border-right:0}
.main-nav li.active{background:var(--rust)}
.hero{left:75px;top:187px;width:743px;height:307px;background:#4d4a44;padding:4px}
.hero-photo{width:100%;height:100%;background:linear-gradient(120deg,#7a6a52 0%,#c9a567 35%,#e6c98a 55%,#a7845a 80%,#6a5842 100%)}
.hero-card{left:96px;top:254px;width:300px;height:131px;background:rgba(179,67,42,.9);color:#fff;padding:10px 13px}
.hero-card h1{font-weight:400;font-size:24px;line-height:30px;margin-bottom:6px}
.hero-card p{font-size:10px;line-height:16.5px}
.panel{left:76px;top:494px;width:740px;height:556px;background:var(--panel)}
.mission{left:76px;top:508px;width:740px;text-align:center}
.mission h2{font-family:"Merriweather",Georgia,serif;font-weight:400;font-size:28px;color:#2e2e2e}
.mission p{font-size:11px;color:var(--muted);line-height:18.5px;margin-top:8px}
.rule{left:99px;width:696px;height:1px;background:var(--rule)}
.video{left:99px;top:627px;width:342px;height:193px;background:linear-gradient(160deg,#6f9a3a,#a9c96a 50%,#4d6e2a)}
.video-bar{left:99px;top:627px;width:342px;height:21px;background:rgba(0,0,0,.75);color:#fff;font-size:9.5px;line-height:21px;padding-left:7px}
.play{left:246px;top:700px;width:38px;height:38px;border-radius:50%;background:rgba(30,30,30,.85)}
.fv-icon{left:457px;top:630px;width:34px;height:34px;border-radius:50%;background:#e6e6e6}
.fv-title{left:501px;top:628px;font-family:"Merriweather",Georgia,serif;font-size:19px;color:#2e2e2e}
.fv-sub{left:501px;top:656px;font-size:9.5px;font-style:italic;color:#888}
.fv-text{left:456px;top:680px;width:340px;font-size:9.5px;line-height:15px;color:var(--muted)}
.btn{left:458px;top:755px;width:109px;height:27px;background:linear-gradient(#d0603f,#b3482c);color:#3a1a10;font-size:10px;font-weight:600;text-align:center;line-height:27px;border-radius:2px}
.news-bar{top:863px;width:345px;height:30px;background:var(--bar);border-radius:12px;color:#fff;font-family:"Merriweather",Georgia,serif;font-weight:700;font-size:15px;line-height:30px;padding-left:19px}
.news-bar .arrows{position:absolute;right:30px;top:0;font-family:"Open Sans",sans-serif;font-weight:400;font-size:13px;color:#ddd}
.news-divider{left:449px;top:865px;height:140px;border-left:1px dashed #999}
.news-list{width:335px}
.news-item{margin-bottom:18px}
.news-item h3{font-size:10px;font-weight:600;color:#333;line-height:16px}
.news-item p{font-size:9.5px;line-height:14px;color:#444}
.news-item a{color:var(--rust);font-style:italic;margin-left:20px;text-decoration:none}
.site-footer{left:0;top:1050px;width:892px;height:150px;background:var(--footer)}
.foot-col{top:1068px;color:var(--footer-text)}
.foot-col h4{font-size:14px;font-weight:600;margin-bottom:6px}
.foot-col li{list-style:none;font-size:9px;line-height:17.4px;padding-left:2px}
.foot-brand{left:604px;top:1070px;display:flex;align-items:center;gap:6px}
.foot-mark{width:30px;height:45px;background:#777}
.foot-name{font-size:15px;color:#ddd;line-height:22px}
.foot-tag{font-size:12px;color:#ddd;line-height:20px;letter-spacing:1px}
.copyright{left:575px;top:1125px;width:190px;text-align:center;font-size:9.5px;line-height:18px;color:#eee}
.social{left:619px;top:1166px;display:flex;gap:7px}
.social span{width:20px;height:20px;border-radius:50%;background:#fff}
</style>
</head>
<body>
<header class="abs site-header"></header>
<div class="abs brand">
  <div class="brand-mark"></div>
  <div><div class="brand-name">Tidewell Botanics</div><div class="brand-tag">organic soap</div></div>
</div>
<div class="abs util-links">Sign In<span>|</span>Register<span>|</span>Contact Us</div>
<div class="abs search">Search...</div>
<div class="abs search-btn"><svg width="18" height="20" viewBox="0 0 18 20"><circle cx="8" cy="9" r="4" fill="none" stroke="#fff" stroke-width="1.6"/><line x1="11" y1="12" x2="14" y2="15" stroke="#fff" stroke-width="1.8"/></svg></div>
<div class="abs cart">Cart</div>
<div class="abs cart-count">0</div>
<nav class="abs main-nav"><ul>
  <li class="active">Home</li><li style="padding:0 34px">Soaps</li><li style="padding:0 30px">Body Butter</li><li style="padding:0 30px">One for One</li><li style="padding:0 28px">Skin Facts</li><li style="padding:0 30px">About</li><li>Contact</li>
</ul></nav>

<section class="abs hero"><div class="hero-photo" role="img" aria-label="Stacked bars of handmade organic soap tied with twine on burlap"></div></section>
<div class="abs hero-card">
  <h1>Tidewell Organic Soap</h1>
  <p>simply dummy text of the printing and typesetting indus-<br>try. Lorem Ipsum has been the industry's standard dummy<br>text ever since &nbsp;the printing and typesetting industry.<br>Lorem Ipsum 1500s &nbsp;&nbsp;⟶</p>
</div>

<main class="abs panel"></main>
<div class="abs mission">
  <h2>Every day 10,000 trees are cut down.</h2>
  <p>Are you just watching or wanna be a part of us to protect those trees<br>Donec sed odio dui. Duis mollis, est non commodo luctus, nisi erat porttitor ia</p>
</div>
<div class="abs rule" style="top:604px"></div>

<div class="abs video" role="img" aria-label="Video still of bundled green vegetables with the word Organic"></div>
<div class="abs video-bar">Hearthfield Aid Charity Video - Help End Poverty</div>
<div class="abs play"><svg width="38" height="38"><polygon points="15,11 28,19 15,27" fill="#fff"/></svg></div>
<div class="abs fv-icon"><svg width="34" height="34"><polygon points="14,12 22,17 14,22" fill="#ccc"/></svg></div>
<div class="abs fv-title">Featured Video</div>
<div class="abs fv-sub">Mollis Ipsum Tortor Vulputate</div>
<p class="abs fv-text">Vestibulum id ligula porta felis euismod semper. Sed posuere consectetur est at lobortis. Donec id elit non mi porta gravida at eget metus. Lorem ipsum do lor sit amet, consectetur adipiscing elit. Cras mattis consectetur purus sit am et fermentum.Aenean lacinia bibendum nulla sed.</p>
<div class="abs btn">Contribute Now</div>
<div class="abs rule" style="top:850px"></div>

<div class="abs news-bar" style="left:85px">Latest News<span class="arrows">‹ ›</span></div>
<div class="abs news-bar" style="left:465px">Upcoming News<span class="arrows">‹ ›</span></div>
<div class="abs news-divider"></div>
<div class="abs news-list" style="left:100px;top:901px">
  <div class="news-item"><h3>Lorem Ipsum is simply dummy printing &nbsp;typesetting.</h3><p>when an unknown printer took a galley of type and scra mbled it to make type specimen book.<a>Read more.</a></p></div>
  <div class="news-item"><h3>Lorem Ipsum is simply dummy printing &nbsp;typesetting.</h3><p>when an unknown printer took a galley of type and scra mbled it to make type specimen book.<a>Read more.</a></p></div>
</div>
<div class="abs news-list" style="left:474px;top:899px">
  <div class="news-item"><h3>Lorem Ipsum is simply dummy printing &nbsp;typesetting.</h3><p>when an unknown printer took a galley of type and scra mbled it to make type specimen book.<a>Read more.</a></p></div>
  <div class="news-item"><h3>Lorem Ipsum is simply dummy printing &nbsp;typesetting.</h3><p>when an unknown printer took a galley of type and scra mbled it to make type specimen book.<a>Read more.</a></p></div>
</div>

<footer class="abs site-footer"></footer>
<div class="abs foot-col" style="left:83px"><h4>WHO WE ARE</h4><ul><li>Company</li><li>News</li><li>Team</li><li>Careers</li><li>Contact</li></ul></div>
<div class="abs foot-col" style="left:221px"><h4>WHAT WE DO</h4><ul><li>What is Tidewell Botanics ?</li><li>Live Demo</li><li>Resources</li><li>FAQs</li><li>Mobile Apps</li></ul></div>
<div class="abs foot-col" style="left:378px"><h4>WHO WE WORK WITH</h4><ul><li>Utilities</li><li>Consumers</li><li>Partners</li><li>Get Started</li></ul></div>
<div class="abs foot-brand"><div class="foot-mark"></div><div><div class="foot-name">Tidewell Botanics</div><div class="foot-tag">organic soap</div></div></div>
<div class="abs copyright">2006 - 2013 &nbsp;&nbsp;Privacy Policy Terms of Conditions. All Rights Reserved</div>
<div class="abs social"><span></span><span></span><span></span><span></span><span></span></div>
</body>
</html>
```